Playing Card Design for Magician's Business Card

Hello! I am looking for a two-sided design for a business card.
The back of the card look like the back of a playing card and includes the following text:
Dorian Feldhaus
www.FeldWonders.com
BACK:
Please - focus most of your time and effort on the BACK DESIGN.
Make it look like a playing card.
I plan to use this design to print up custom playing cards that I use in my show and give away to guests.
No Bunnies No Top Hats!
Not for kids. This is for sophisticated sleight of hand performed for adults.
Mood: Slick, elegant + fun.
See the attached samples of cards I like.
FRONT:
Not much text required ... Please leave plenty of blank space - minimalist.
The front of the card will have
First Name
Website
Phone Number
Email Address
Target Market(s)
Event Planners
Targeting corporate special events and private parties.
Industry/Entity Type
Magician
Contact Information for Business Card
Dorian Feldhaus
Illusionist
www.FeldWonders.com
Colors
Designer to choose colors to be used in the design.
Requirements
Must have
- Back must look like a playing card back.
- BACK MUST INCLUDE the following text:
- Dorian Feldhaus
- www.FeldWonders.com
Nice to have
- Symmetrical Design for back so the card looks the same if upside down.
- Please see "All Seeing Eye" design attached. Remove the Latin phrase and replace with Dorian (top left) Feldhaus (top right)
- FeldWonders.com (Lower middle)
Should not have
- Bunny Rabbits
- Top Hats
- Kids ....

```html
<!DOCTYPE html>
<html lang="en">
<head>
<meta charset="utf-8">
<title>Dorian Feldhaus — Illusionist Business Card</title>
<link href="https://fonts.googleapis.com/css2?family=Almendra:wght@400&family=Federo&display=swap" rel="stylesheet">
<style>
  :root {
    --backdrop: #9b9b9b;
    --card-ink: #050505;
    --card-line: #efefef;
    --ornament-light: #9a9a9a;
    --ornament-dark: #3c3c3c;
  }
  * { margin: 0; padding: 0; box-sizing: border-box; }
  html, body { width: 1200px; height: 900px; overflow: hidden; }
  body { background: var(--backdrop); position: relative; }
  .card {
    position: absolute;
    top: 214px;
    width: 270px;
    height: 474px;
    border-radius: 18px;
    overflow: hidden;
    background: var(--card-ink);
  }
  .card--back { left: 289px; }
  .card--front { left: 641px; }
  .card svg { position: absolute; inset: 0; width: 100%; height: 100%; }
  .back-label {
    position: absolute;
    left: 0; right: 0;
    text-align: center;
    color: var(--card-line);
    font-family: "Almendra", serif;
    font-size: 11.5px;
    letter-spacing: 0.3px;
    line-height: 14px;
  }
  .back-label--name { top: 55px; }
  .back-label--site {
    top: 405px;
    font-family: "Federo", sans-serif;
    font-size: 10px;
    transform: rotate(180deg);
  }
  .contact {
    position: absolute;
    left: 0; right: 0;
    text-align: center;
    color: var(--card-line);
  }
  .contact__name {
    top: 235px;
    font-family: "Almendra", serif;
    font-size: 21px;
    letter-spacing: 0.2px;
  }
  .contact__role {
    top: 270px;
    font-family: "Federo", sans-serif;
    font-size: 12px;
    letter-spacing: 0.4px;
  }
  .contact__details {
    top: 308px;
    font-family: "Federo", sans-serif;
    font-size: 14.5px;
    line-height: 22px;
    letter-spacing: 0.3px;
  }
</style>
</head>
<body>

<!-- Playing-card back -->
<div class="card card--back">
  <svg viewBox="0 0 270 474" xmlns="http://www.w3.org/2000/svg">
    <defs>
      <radialGradient id="scrollTone" cx="50%" cy="50%" r="65%">
        <stop offset="0" stop-color="var(--ornament-light)"/>
        <stop offset="1" stop-color="var(--ornament-dark)"/>
      </radialGradient>
      <linearGradient id="medallionTone" x1="0" y1="0" x2="0" y2="1">
        <stop offset="0" stop-color="var(--ornament-dark)"/>
        <stop offset="0.5" stop-color="var(--ornament-light)"/>
        <stop offset="1" stop-color="var(--ornament-dark)"/>
      </linearGradient>
    </defs>
    <rect class="ornament-field" x="10" y="16" width="250" height="442" fill="url(#scrollTone)" role="img" aria-label="Interlaced scroll border pattern"/>
    <rect x="36" y="88" width="198" height="298" fill="none" stroke="var(--card-line)" stroke-width="3"/>
    <polygon class="center-medallion" points="135,89 227,237 135,386 44,237" fill="url(#medallionTone)" stroke="var(--card-line)" stroke-width="6" role="img" aria-label="Symmetrical scrolled medallion ornament"/>
    <g class="corner-seals" fill="var(--card-ink)" stroke="var(--card-line)">
      <circle cx="8" cy="8" r="88" stroke-width="7"/>
      <circle cx="262" cy="8" r="88" stroke-width="7"/>
      <circle cx="8" cy="466" r="88" stroke-width="7"/>
      <circle cx="262" cy="466" r="88" stroke-width="7"/>
      <circle cx="27" cy="33" r="20" stroke-width="3.5"/>
      <circle cx="243" cy="33" r="20" stroke-width="3.5"/>
      <circle cx="27" cy="441" r="20" stroke-width="3.5"/>
      <circle cx="243" cy="441" r="20" stroke-width="3.5"/>
    </g>
  </svg>
  <div class="back-label back-label--name">Dorian Feldhaus</div>
  <div class="back-label back-label--site">www.FeldWonders.com</div>
</div>

<!-- Contact face -->
<div class="card card--front">
  <svg viewBox="0 0 270 474" xmlns="http://www.w3.org/2000/svg">
    <defs>
      <linearGradient id="bandTone" x1="0" y1="0" x2="1" y2="0">
        <stop offset="0" stop-color="var(--ornament-dark)"/>
        <stop offset="0.5" stop-color="var(--ornament-light)"/>
        <stop offset="1" stop-color="var(--ornament-dark)"/>
      </linearGradient>
      <linearGradient id="columnTone" x1="0" y1="0" x2="0" y2="1">
        <stop offset="0" stop-color="var(--ornament-dark)"/>
        <stop offset="0.5" stop-color="var(--ornament-light)"/>
        <stop offset="1" stop-color="var(--ornament-dark)"/>
      </linearGradient>
    </defs>
    <rect x="10" y="19" width="250" height="27" fill="url(#bandTone)" role="img" aria-label="Scroll border band"/>
    <rect x="10" y="427" width="250" height="27" fill="url(#bandTone)" role="img" aria-label="Scroll border band"/>
    <rect x="10" y="89" width="33" height="298" fill="url(#columnTone)" role="img" aria-label="Scroll border column"/>
    <rect x="227" y="89" width="33" height="298" fill="url(#columnTone)" role="img" aria-label="Scroll border column"/>
    <rect class="info-panel" x="45" y="46" width="180" height="381" fill="var(--card-ink)" stroke="var(--card-line)" stroke-width="4"/>
    <path class="crest-area" d="M135 50 C115 90 72 120 76 150 C82 175 118 168 135 150 C152 168 188 175 194 150 C198 120 155 90 135 50 Z" fill="url(#columnTone)" role="img" aria-label="Flourished crest ornament"/>
    <g class="corner-seals" fill="var(--card-ink)" stroke="var(--card-line)">
      <circle cx="8" cy="8" r="88" stroke-width="7"/>
      <circle cx="262" cy="8" r="88" stroke-width="7"/>
      <circle cx="8" cy="466" r="88" stroke-width="7"/>
      <circle cx="262" cy="466" r="88" stroke-width="7"/>
      <circle cx="27" cy="33" r="20" stroke-width="3.5"/>
      <circle cx="243" cy="33" r="20" stroke-width="3.5"/>
      <circle cx="27" cy="441" r="20" stroke-width="3.5"/>
      <circle cx="243" cy="441" r="20" stroke-width="3.5"/>
    </g>
  </svg>
  <div class="contact contact__name">Dorian Feldhaus</div>
  <div class="contact contact__role">Illusionist</div>
  <div class="contact contact__details">
    555-201-7394<br>
    info@FeldWonders.com<br>
    www.FeldWonders.com
  </div>
</div>

</body>
</html>
```